Career Development Program Flyer

Freshen up the look and make it more promotional. We want our teachers to know about the career tracks we offer. This document spells it all out, but we want it to pop! This will be a tool to help attract new applicants who are interested in future growth as well as retain our current staff who are interested in promotional opportunities.

Target Market(s)

our current teachers looking for growth or applicants interviewing who are interested in future growth with the company

Font styles to use
Serif
Sans Serif

Colors
3277b5
0255a3
cedeed
fbee3f
85acd3
fbf289

Requirements
Must have
• -our logo (i can send a new version if needed)
• -the information in the document provided
• -for more information on our company visit www.brightfernlearninghub.com

```html
<!DOCTYPE html>
<html lang="en">
<head>
<meta charset="utf-8">
<title>Career Growth Program Flyer</title>
<link href="https://fonts.googleapis.com/css2?family=Anton&family=Oswald:wght@600;700&family=Roboto+Condensed:ital,wght@0,400;0,500;0,700;1,400&display=swap" rel="stylesheet">
<style>
  :root {
    --backdrop: #5e5e5e;
    --paper: #ffffff;
    --brand-blue: #0a5cb4;
    --deep-blue: #0543b8;
    --fresh-green: #3cb54a;
    --title-green: #34ad3c;
    --accent-red: #a80c0c;
    --body-grey: #4a4a4a;
    --photo-warm: #e9d3bf;
    --photo-cool: #c9cfd6;
  }
  * { box-sizing: border-box; margin: 0; padding: 0; }
  html, body { width: 1200px; height: 1200px; overflow: hidden; background: var(--backdrop); }
  body { font-family: "Roboto Condensed", "Arial Narrow", sans-serif; }

  .flyer {
    position: absolute; left: 246px; top: 120px;
    width: 725px; height: 952px; background: var(--paper); overflow: hidden;
  }
  .flyer-shapes { position: absolute; inset: 0; }

  .headline { position: absolute; left: 40px; top: 282px; }
  .headline-career { font-family: "Anton", sans-serif; font-size: 80px; line-height: 1; color: var(--brand-blue); letter-spacing: 0.5px; }
  .headline-growth { font-family: "Oswald", sans-serif; font-weight: 700; font-size: 42px; line-height: 1; color: var(--brand-blue); margin-top: 0; }
  .headline-sub { font-weight: 500; font-size: 33px; line-height: 1.1; color: var(--title-green); margin-top: 6px; }
  .headline-rule { width: 40px; height: 3px; background: var(--brand-blue); margin-top: 10px; }

  .teacher-column { position: absolute; left: 40px; top: 462px; width: 350px; }
  .section-title { font-weight: 500; font-size: 22px; color: var(--brand-blue); line-height: 1.2; }
  .role-title { font-weight: 500; font-size: 15.5px; color: var(--title-green); margin-top: 12px; line-height: 1.2; }
  .section-title + .role-title { margin-top: 2px; }
  .role-list { list-style: none; margin-top: 4px; }
  .role-list li {
    position: relative; padding-left: 19px; font-size: 14.5px; line-height: 17.6px;
    color: var(--body-grey); margin-bottom: 4px;
  }
  .role-list li::before {
    content: ""; position: absolute; left: 1px; top: 4px; width: 9px; height: 9px;
    border-radius: 50%; border: 2.5px solid var(--brand-blue);
  }

  .aide-header {
    position: absolute; left: 406px; top: 254px; width: 276px; height: 86px;
    background: var(--accent-red); border-radius: 24px 24px 0 0;
    padding: 20px 0 0 32px;
    font-family: "Oswald", sans-serif; font-weight: 700; font-size: 23px; line-height: 1.15; color: #fff;
  }
  .aide-panel {
    position: absolute; left: 406px; top: 340px; width: 276px; height: 296px;
    background: var(--fresh-green); padding: 20px 8px 0 30px; color: #fff;
  }
  .aide-title { font-weight: 500; font-size: 15.5px; line-height: 19px; margin-top: 12px; }
  .aide-title:first-child { margin-top: 0; }
  .aide-list { list-style: none; margin-top: 3px; }
  .aide-list li { position: relative; padding-left: 18px; font-weight: 500; font-size: 14px; line-height: 17.5px; }
  .aide-list li::before {
    content: ""; position: absolute; left: 1px; top: 4px; width: 8px; height: 8px;
    border: 2px solid #fff; border-radius: 2px; background: var(--brand-blue);
  }

  .admin { position: absolute; left: 412px; top: 664px; width: 300px; }
  .admin .section-title { font-size: 22px; }
  .admin-note { font-style: italic; font-size: 14px; color: var(--accent-red); margin-top: 2px; }
  .admin-list { list-style: none; display: grid; grid-template-columns: 140px 140px; row-gap: 1px; margin-top: 6px; }
  .admin-list li { position: relative; padding-left: 16px; font-weight: 500; font-size: 15px; color: var(--title-green); line-height: 18.5px; }
  .admin-list li::before {
    content: ""; position: absolute; left: 0; top: 5px; width: 8px; height: 8px;
    border-radius: 50%; border: 2.5px solid var(--brand-blue);
  }

  .brand { position: absolute; left: 406px; top: 782px; width: 280px; text-align: center; }
  .brand-dot { display: block; width: 30px; height: 30px; border-radius: 50%; background: var(--brand-blue); margin: 0 auto 4px; }
  .brand-name { font-weight: 400; font-size: 27px; line-height: 1.1; color: var(--brand-blue); white-space: nowrap; }
  .brand-tagline { font-size: 6.6px; letter-spacing: 1.3px; color: var(--brand-blue); margin-top: 5px; white-space: nowrap; }

  .footer-item { position: absolute; display: flex; align-items: center; gap: 10px; color: #fff; font-weight: 700; font-size: 14px; }
  .footer-phone { left: 40px; top: 924px; }
  .footer-web { left: 186px; top: 924px; }
  .footer-address { left: 476px; top: 902px; line-height: 16px; font-size: 13px; }
</style>
</head>
<body>
<main class="flyer">
  <svg class="flyer-shapes" width="725" height="952" viewBox="0 0 725 952" aria-hidden="false">
    <defs>
      <linearGradient id="photoTone" x1="0" y1="0" x2="1" y2="1">
        <stop offset="0" stop-color="var(--photo-cool)"/>
        <stop offset="0.5" stop-color="var(--photo-warm)"/>
        <stop offset="1" stop-color="#e6e2c4"/>
      </linearGradient>
    </defs>
    <rect x="0" y="0" width="725" height="400" fill="url(#photoTone)" role="img" aria-label="Photo of a smiling teacher with a young girl in a bright classroom"/>
    <path d="M0,345 C70,252 130,226 190,228 C280,232 360,300 420,345 L725,345 L725,952 L0,952 Z" fill="var(--paper)"/>
    <path d="M112,238 C150,228 180,226 200,229 C285,236 355,296 412,342" fill="none" stroke="var(--accent-red)" stroke-width="3"/>
    <path d="M682,392 C700,384 716,372 725,352 L725,372 C713,388 700,396 682,401 Z" fill="var(--accent-red)"/>
    <path d="M0,910 L378,910 C392,910 394,880 412,880 L725,880 L725,952 L0,952 Z" fill="var(--deep-blue)"/>
    <path d="M200,910 L378,910 C392,910 394,880 412,880 L440,880" fill="none" stroke="var(--accent-red)" stroke-width="2"/>
  </svg>

  <header class="headline">
    <div class="headline-career">Career</div>
    <div class="headline-growth">Growth Program</div>
    <div class="headline-sub">Qualifications by Position</div>
    <div class="headline-rule"></div>
  </header>

  <section class="teacher-column">
    <h2 class="section-title">Infant and Preschool Teacher Positions</h2>
    <h3 class="role-title">Infant or Preschool Assistant Teacher</h3>
    <ul class="role-list"><li>Entry level teachers</li><li>12 ECE units minimum</li></ul>
    <h3 class="role-title">Infant or Preschool Assistant Teacher</h3>
    <ul class="role-list"><li>Entry level teachers</li><li>12 ECE units minimum</li></ul>
    <h3 class="role-title">Infant or Preschool Assistant Teacher</h3>
    <ul class="role-list">
      <li>Minimum to qualify: B.A. Degree in Child Development with 2 years’ experience or B.A. Degree in any subject with 12 ECE units and 7+ years’ experience</li>
      <li>Professional, enthusiastic and influential role model to their peers at both their sites as well as other BFLH locations</li>
    </ul>
    <h3 class="role-title">Infant or Preschool Assistant Teacher</h3>
    <ul class="role-list">
      <li>Minimum to qualify: AA + 12 ECE units with 2 years experience or 12 ECE units with 5 years’ experience</li>
      <li>Professional, enthusiastic and an influential role model to their peers, specifically those teaching in their age group</li>
    </ul>
  </section>

  <h2 class="aide-header">Infant and Preschool Aide Positions</h2>
  <section class="aide-panel">
    <h3 class="aide-title">Infant or Preschool Aide III Extended Day Staff</h3>
    <ul class="aide-list"><li>0-11 ECE units</li><li>Manages the classroom independently</li><li>At least 3 years’ experience</li></ul>
    <h3 class="aide-title">Infant or Preschool Aide II</h3>
    <ul class="aide-list"><li>0-11 ECE units</li><li>Experience in the field</li></ul>
    <h3 class="aide-title">Infant or Preschool Aide I</h3>
    <ul class="aide-list"><li>No ECE units</li><li>Limited experience</li><li>Training needed</li></ul>
  </section>

  <section class="admin">
    <h2 class="section-title">Administration Positions</h2>
    <p class="admin-note">Not all positions are applicable at every site</p>
    <ul class="admin-list">
      <li>Office Assistant</li><li>Office Administrator</li>
      <li>Assistant Director</li><li>Director</li>
      <li>Senior Director</li>
    </ul>
  </section>

  <div class="brand">
    <span class="brand-dot"></span>
    <div class="brand-name">Bright Fern Learning Hub</div>
    <div class="brand-tagline">PRIVATE INFANT CARE · PRESCHOOL · ELEMENTARY · MIDDLE SCHOOL</div>
  </div>

  <div class="footer-item footer-phone">
    <svg width="17" height="17" viewBox="0 0 24 24"><path fill="#fff" d="M6.6 10.8a15.1 15.1 0 0 0 6.6 6.6l2.2-2.2a1 1 0 0 1 1-.25 11.4 11.4 0 0 0 3.6.57 1 1 0 0 1 1 1V20a1 1 0 0 1-1 1A17 17 0 0 1 3 4a1 1 0 0 1 1-1h3.5a1 1 0 0 1 1 1c0 1.25.2 2.45.57 3.57a1 1 0 0 1-.25 1z"/></svg>
    <span>(408) 555-0143</span>
  </div>
  <div class="footer-item footer-web">
    <svg width="14" height="14" viewBox="0 0 24 24" fill="none" stroke="#fff" stroke-width="2"><circle cx="12" cy="12" r="10"/><path d="M2 12h20M12 2c3 3 3 17 0 20M12 2c-3 3-3 17 0 20"/></svg>
    <span>www.brightfernlearninghub.com</span>
  </div>
  <div class="footer-item footer-address">
    <svg width="18" height="24" viewBox="0 0 24 32"><path fill="#fff" d="M12 0C5.4 0 0 5.4 0 12c0 9 12 20 12 20s12-11 12-20C24 5.4 18.6 0 12 0zm0 17a5 5 0 1 1 0-10 5 5 0 0 1 0 10z"/></svg>
    <span>1450 Willow Crest Avenue, Building C<br>San Jose, CA 95126</span>
  </div>
</main>
</body>
</html>
```